BANNER FOR ONLINE CABINET COMPANY MAIN PAGE

Need 3 different banners for the main page. We are online platform for ordering cabinets, parts etc. online.
Website: trimfit.ca
A place where the banner will be placed: https://view.snapvault.example/qR7TpWzKmB4eX
Banner size: 1344x399 pixels
****Clients should get the main point that they can order everything online through the website.

Industry/Entity Type

online cabinets and parts ordering

Requirements
Must have
• online ordering icons, iphone, laptop, desktop pc - so clients get an idea that this is web based service to order cabinets

```html
<!DOCTYPE html>
<html lang="en">
<head>
<meta charset="utf-8">
<title>TrimFit – Veneer Doors &amp; Fronts</title>
<link href="https://fonts.googleapis.com/css2?family=Archivo:wght@400;700;800&family=Montserrat:wght@700;800&family=Poppins:wght@300;400;600&display=swap" rel="stylesheet">
<style>
  :root {
    --page-dark: #13171b;
    --nav-bg: #2b2d30;
    --nav-text: #e6e6e6;
    --order-green: #4caf50;
    --heading-band: #e4e5e7;
    --heading-ink: #111111;
    --sub-ink: #4a4a4a;
    --brand-red: #f0454f;
    --band-red: rgba(226, 60, 66, 0.82);
    --button-dark: #3a3a3a;
    --white: #ffffff;
    --dot-grey: #cfcfcf;
    --dot-active: #f0a030;
    --chat-navy: #2f3552;
  }
  * { margin: 0; padding: 0; box-sizing: border-box; }
  html, body { width: 1200px; height: 1200px; overflow: hidden; background: var(--page-dark); }
  .canvas { position: relative; width: 1200px; height: 1200px; background: var(--page-dark); font-family: "Archivo", Arial, sans-serif; }

  .site { position: absolute; left: 0; top: 269px; width: 1200px; height: 551px; background: var(--white); overflow: hidden; }

  .nav { position: absolute; left: 0; top: 0; width: 1200px; height: 32px; background: var(--nav-bg); color: var(--nav-text); font-size: 7.5px; }
  .nav > * { position: absolute; top: 50%; transform: translateY(-50%); white-space: nowrap; }
  .brand { left: 27px; font-weight: 700; font-size: 13px; color: var(--white); }
  .divider { left: 101px; width: 1px; height: 18px; background: var(--white); }
  .tagline { left: 112px; }
  .contact-box { left: 209px; width: 199px; height: 16px; background: #000; display: flex; align-items: center; gap: 6px; padding-left: 7px; font-size: 6.5px; }
  .contact-box svg { width: 9px; height: 9px; }
  .nav-link { text-transform: uppercase; letter-spacing: 0.2px; }
  .order-now { left: 727px; width: 62px; height: 13px; border-radius: 7px; background: var(--order-green); color: var(--white); text-align: center; line-height: 13px; font-size: 7px; }
  .nav-icon { width: 11px; height: 11px; }

  .heading-band { position: absolute; left: 0; top: 32px; width: 1200px; height: 57px; background: var(--heading-band); text-align: center; }
  .heading-band h1 { position: absolute; left: 0; right: 0; top: 3px; font-weight: 800; font-size: 18px; color: var(--heading-ink); letter-spacing: 0.3px; }
  .heading-band p { position: absolute; left: 0; right: 0; top: 30px; font-size: 13px; color: var(--sub-ink); }

  .hero { position: absolute; left: 0; top: 89px; width: 1200px; height: 359px; }
  .hero-backdrop { position: absolute; inset: 0; background: linear-gradient(90deg, #e9e9ea 0%, #dcdcdc 35%, #d3d0cd 65%, #d6d4d2 100%); }
  .hero-title { position: absolute; left: 42px; top: 38px; font-family: "Poppins", sans-serif; font-weight: 400; font-size: 59px; line-height: 59px; color: var(--brand-red); letter-spacing: -1px; }
  .red-band { position: absolute; left: 0; top: 236px; width: 1200px; height: 123px; background: var(--band-red); }
  .photo-frame { position: absolute; left: 357px; top: 25px; width: 806px; height: 229px; }
  .choose { position: absolute; left: 40px; top: 254px; font-family: "Montserrat", sans-serif; font-weight: 700; font-size: 21px; line-height: 27.5px; color: var(--white); }
  .cta { position: absolute; left: 561px; top: 237px; width: 396px; height: 85px; border-radius: 43px; background: linear-gradient(180deg, #5a5a5a 0%, var(--button-dark) 60%, #2a2a2a 100%); box-shadow: 0 4px 10px rgba(0,0,0,0.35); color: var(--white); font-family: "Montserrat", sans-serif; font-weight: 800; font-size: 26.5px; display: flex; align-items: center; justify-content: center; letter-spacing: 0.2px; }

  .device-icons { position: absolute; left: 985px; top: 268px; width: 190px; height: 70px; }

  .slider-dots { position: absolute; left: 551px; top: 453px; display: flex; gap: 8px; }
  .slider-dots span { width: 7px; height: 7px; background: var(--dot-grey); }
  .slider-dots .active { background: var(--dot-active); }

  .section-title { position: absolute; left: 0; right: 0; top: 481px; text-align: center; font-weight: 700; font-size: 17.5px; color: var(--heading-ink); letter-spacing: 0.3px; }

  .chat-tab { position: absolute; left: 1034px; top: 531px; width: 151px; height: 20px; border-radius: 6px 6px 0 0; background: var(--chat-navy); color: var(--white); font-size: 6.5px; line-height: 20px; padding-left: 9px; white-space: nowrap; }
  .chat-tab::after { content: ""; position: absolute; right: -3px; top: -2px; width: 11px; height: 11px; border-radius: 50%; background: var(--order-green); }
</style>
</head>
<body>
<div class="canvas">
  <div class="site">

    <header class="nav">
      <span class="brand">TrimFit</span>
      <span class="divider"></span>
      <span class="tagline">Got the size you need!</span>
      <span class="contact-box">
        <svg viewBox="0 0 24 24" aria-hidden="true"><path fill="#fff" d="M6.6 10.8a15 15 0 0 0 6.6 6.6l2.2-2.2a1 1 0 0 1 1-.25 11.4 11.4 0 0 0 3.6.57 1 1 0 0 1 1 1V20a1 1 0 0 1-1 1A17 17 0 0 1 3 4a1 1 0 0 1 1-1h3.5a1 1 0 0 1 1 1c0 1.25.2 2.45.57 3.57a1 1 0 0 1-.25 1z"/></svg>
        <span>Call us (555) 014 2290</span>
        <svg viewBox="0 0 24 24" aria-hidden="true" style="margin-left:10px"><circle cx="12" cy="12" r="9" fill="none" stroke="#fff" stroke-width="2.5"/><path d="M12 7v5l3 2" fill="none" stroke="#fff" stroke-width="2.5"/></svg>
        <span>Mon-Fri 8AM - 4:30PM</span>
      </span>
      <span class="nav-link" style="left:699px">CAD</span>
      <span class="order-now">ORDER NOW</span>
      <span class="nav-link" style="left:802px">Design &amp; Quote</span>
      <span class="nav-link" style="left:876px">Samples</span>
      <span class="nav-link" style="left:923px">About</span>
      <span class="nav-link" style="left:962px">Contact</span>
      <span class="nav-link" style="left:1010px">Articles</span>
      <svg class="nav-icon" style="left:1067px" viewBox="0 0 24 24" aria-hidden="true"><circle cx="10" cy="10" r="6" fill="none" stroke="#e6e6e6" stroke-width="2"/><path d="M15 15l5 5" stroke="#e6e6e6" stroke-width="2"/></svg>
      <span style="left:1106px;font-size:14px;font-weight:800;color:#fff">?</span>
      <svg class="nav-icon" style="left:1140px" viewBox="0 0 24 24" aria-hidden="true"><circle cx="12" cy="8" r="4" fill="none" stroke="#e6e6e6" stroke-width="2"/><path d="M4 21c1-5 15-5 16 0z" fill="none" stroke="#e6e6e6" stroke-width="2"/></svg>
      <svg class="nav-icon" style="left:1175px" viewBox="0 0 24 24" aria-hidden="true"><path d="M2 4h3l3 11h11l2-8H7" fill="none" stroke="#e6e6e6" stroke-width="2"/><circle cx="9" cy="19" r="1.6" fill="#e6e6e6"/><circle cx="18" cy="19" r="1.6" fill="#e6e6e6"/></svg>
    </header>

    <section class="heading-band">
      <h1>THE FIRST ONLINE CUSTOM CABINET’S MANUFACTURER</h1>
      <p>Order custom cabinets online with instant price calculator. No hidden fees, top quality warranty.</p>
    </section>

    <section class="hero">
      <div class="hero-backdrop" role="img" aria-label="Soft-focus background photo of a bright modern kitchen"></div>
      <div class="red-band"></div>
      <h2 class="hero-title">VENEER<br>DOORS &amp;<br>FRONTS</h2>
      <svg class="photo-frame" viewBox="0 0 806 229" role="img" aria-label="Photo of a modern kitchen with white and walnut veneer cabinets, stainless appliances and a white island">
        <defs>
          <linearGradient id="kitchenTones" x1="0" y1="0" x2="1" y2="1">
            <stop offset="0" stop-color="#e6e6e6"/>
            <stop offset="0.55" stop-color="#d2cdc8"/>
            <stop offset="1" stop-color="#c9b6a6"/>
          </linearGradient>
        </defs>
        <path d="M60 0 H806 V160 Q806 229 737 229 H0 V60 Q0 0 60 0 Z" fill="#ffffff"/>
        <path d="M62 8 H798 V158 Q798 221 735 221 H8 V62 Q8 8 62 8 Z" fill="url(#kitchenTones)"/>
      </svg>
      <p class="choose">Choose from :<br>Walnut Veneer - Maple Veneer<br>Red Oak Veneer - White Oak Veneer</p>
      <a class="cta">GET THE INSTANT PRICE</a>

      <svg class="device-icons" viewBox="0 0 190 70" role="img" aria-label="Order online from phone, laptop or desktop">
        <g fill="none" stroke="#ffffff" stroke-width="3" stroke-linejoin="round" stroke-linecap="round">
          <rect x="6" y="14" width="26" height="46" rx="5"/>
          <path d="M15 20h8"/>
          <circle cx="19" cy="53" r="1.5" fill="#ffffff"/>
          <rect x="54" y="20" width="50" height="32" rx="3"/>
          <path d="M46 58h66l-5-6H51z"/>
          <rect x="126" y="10" width="58" height="40" rx="3"/>
          <path d="M148 50l-3 10M162 50l3 10M140 60h30"/>
        </g>
      </svg>
    </section>

    <div class="slider-dots"><span></span><span></span><span></span><span></span><span class="active"></span><span></span><span></span></div>

    <h2 class="section-title">EASY QUOTE &amp; ORDER</h2>

    <div class="chat-tab">Questions? Start chat, we are online!</div>
  </div>
</div>
</body>
</html>
```